Varrowick Biomedical Research Institute (VBRI) Web Design

VBRI is a non-profit organization focused on saving the lives of terminally ill patients by becoming the leaders in cutting-edge research, innovative technologies, utilizing national and international partnerships as well as the associated allopathic and naturopathic treatments necessary to do so.

Our primary focus is raising funds to support the research and acquisition of new technologies for life saving treatments which are NOT a one size fits all approach like conventional medicine but rather a marriage of the latest technologies used in combination with other new treatment possibilities for a successful end result.

Our domain is varrowickbr.org

Logo files are attached.

Looking for something clean, light, healthy.

Target Market(s)

The site should look and feel towards research/scientific grant writing.
Medical professionals, Medical Scientists.

Industry/Entity Type

Medical And Science

Number of Pages Required

4 page

Requirements
Nice to have
• Here are examples of sites I like in the order of how much I like them.
• https://www.palvenhope.org/give.html
• https://www.thekqtf.org/donate-to-kqtf
• https://www.curewaveinst.org/we-are-cwi/join-the-cause
• https://www.healquest.org/involved/donate.html
• https://give.nptf.org/checkout/donation?eid=58217
• https://www.moravind.org/how-you-can-help
• https://donate3.healquest.org/

```html
<!DOCTYPE html>
<html lang="en">
<head>
<meta charset="utf-8">
<title>Varrowick Biomedical Research Institute</title>
<link rel="stylesheet" href="https://fonts.googleapis.com/css2?family=Ubuntu:wght@400;500;700&display=swap">
<style>
  :root{
    --blue:#1a74b8;
    --blue-dark:#155f98;
    --green:#7ab843;
    --green-dark:#6aa536;
    --white:#ffffff;
    --ink:#4a4a4a;
    --hero-a:#c9d0d8;
    --hero-b:#dde2e8;
    --hero-warm:#cdb89e;
  }
  *{margin:0;padding:0;box-sizing:border-box}
  html,body{width:1200px;height:931px;overflow:hidden;background:var(--white)}
  body{font-family:"Ubuntu",sans-serif;position:relative}
  .site-header{position:absolute;left:0;top:0;width:1200px;height:107px;background:var(--white)}
  .brand{position:absolute;left:61px;top:34px;display:flex;align-items:center;gap:12px}
  .brand-dot{width:40px;height:40px;border-radius:50%;background:var(--green)}
  .brand-name{font-size:17px;font-weight:500;color:var(--blue);line-height:1.2;max-width:200px}
  .header-contact{position:absolute;right:62px;top:25px;text-align:right}
  .social{display:flex;justify-content:flex-end;gap:5px}
  .social span{width:28px;height:28px;border-radius:50%;background:var(--blue);display:block}
  .call{margin-top:10px;font-size:14px;color:var(--blue);display:flex;align-items:center;justify-content:flex-end;gap:6px}
  .call b{font-weight:400;font-size:18px}
  .main-nav{position:absolute;left:0;top:107px;width:1200px;height:53px;background:var(--blue)}
  .main-nav ul{list-style:none;display:flex;position:absolute;left:62px;top:0;height:53px}
  .main-nav li{color:var(--white);font-size:15px;display:flex;align-items:center;padding:0 22px;border-right:1px solid var(--blue-dark)}
  .main-nav li:last-child{border-right:none}
  .main-nav li.active{background:var(--blue-dark)}
  .donate-btn{position:absolute;left:981px;top:107px;width:156px;height:61px;background:var(--green);color:var(--white);font-size:15px;display:flex;align-items:center;justify-content:center;gap:8px;text-transform:uppercase}
  .donate-btn .sign{font-size:20px;font-weight:700}
  .hero{position:absolute;left:0;top:160px;width:1200px;height:526px;
    background:linear-gradient(90deg,var(--hero-warm) 0%,#d9d2c8 22%,var(--hero-b) 45%,var(--hero-a) 70%,#d8c7ad 100%)}
  .hero-caption{position:absolute;left:95px;top:580px;width:982px;height:87px;background:var(--green);color:var(--white);padding:15px 11px}
  .hero-caption h2{font-size:16px;font-weight:500}
  .hero-caption p{font-size:15px;line-height:19px}
  .give-tabs{position:absolute;left:0;top:686px;width:1200px;height:245px;background:var(--white)}
  .give-tabs ul{list-style:none;display:flex;justify-content:space-between;padding:0 42px 0 40px;margin-top:50px}
  .give-tabs li{font-size:20px;color:var(--ink)}
</style>
</head>
<body>
  <header class="site-header">
    <div class="brand">
      <span class="brand-dot"></span>
      <span class="brand-name">Varrowick Biomedical Research Institute</span>
    </div>
    <div class="header-contact">
      <div class="social"><span></span><span></span><span></span><span></span></div>
      <div class="call">Call us :
        <svg width="14" height="18" viewBox="0 0 14 18" aria-hidden="true"><path d="M3 1c2 0 3 3 2 4L4 6c1 3 3 6 5 7l1-1c1-1 4 0 4 2 0 2-2 3-4 3C5 16 0 9 0 5 0 3 1 1 3 1z" fill="var(--blue)"/></svg>
        <b>0044 719 203</b></div>
    </div>
  </header>

  <nav class="main-nav">
    <ul>
      <li class="active">About Us</li>
      <li>Care &amp; Treatment</li>
      <li>Research</li>
      <li>Training</li>
      <li>Get Involved</li>
      <li>Way To Give</li>
    </ul>
  </nav>
  <a class="donate-btn"><span class="sign">$</span> Donation</a>

  <section class="hero" role="img" aria-label="Photo of a smiling woman in a head wrap resting her face in her hands"></section>
  <div class="hero-caption">
    <h2>Your contribution extends lives.</h2>
    <p>Make the biggest impact possible by supporting innovative immunotherapy research for all types of cancers. Together, we can change the way cancer is treated and cured.</p>
  </div>

  <section class="give-tabs">
    <ul>
      <li>One Time Donation</li>
      <li>Recurring Donation</li>
      <li>Give A Gift In Honor</li>
      <li>Donate to a fundraiser</li>
      <li>Who can donate</li>
    </ul>
  </section>
</body>
</html>
```